Business Card for my Photography/Video Business

I would like the card to say Event Photographer and Videographer. I like the Black and Gold look to it as well but open to other options. I don't want it to be super vibrant or colorful. Simple, elegant and professional

```html
<!DOCTYPE html>
<html lang="en">
<head>
<meta charset="utf-8">
<title>Nox Studio – Business Card</title>
<link rel="stylesheet" href="https://fonts.googleapis.com/css2?family=Montserrat:wght@500;700&family=Arimo:wght@400&display=swap">
<style>
  :root {
    --backdrop: #2a2724;
    --card: #050505;
    --gold: #a8925f;
    --gold-light: #c4ac75;
    --gold-deep: #8c7748;
    --ink: #0b0a08;
  }
  * { margin: 0; padding: 0; box-sizing: border-box; }
  html, body { width: 1200px; height: 900px; overflow: hidden; }
  body { background: var(--backdrop); position: relative; font-family: "Arimo", Arial, sans-serif; }

  .card {
    position: absolute;
    top: 82px;
    width: 431px;
    height: 738px;
    background: var(--card);
    overflow: hidden;
  }
  .card--front { left: 128px; border-radius: 46px 0 46px 0; }
  .card--back  { left: 643px; border-radius: 0 46px 0 46px; }

  .brand-disc {
    position: absolute;
    border-radius: 50%;
    background: radial-gradient(circle at 40% 35%, var(--gold-light), var(--gold) 55%, var(--gold-deep));
  }
  .front-disc {
    left: 98px; top: 108px; width: 234px; height: 234px;
    display: flex; align-items: center; justify-content: center;
  }
  .front-disc .brand-name {
    font-family: "Montserrat", sans-serif; font-weight: 500;
    font-size: 28px; color: var(--ink);
  }

  .holder-name {
    position: absolute; top: 400px; width: 100%; text-align: center;
    font-family: "Montserrat", sans-serif; font-weight: 700;
    font-size: 21px; letter-spacing: 0.5px; color: var(--gold);
  }
  .holder-role {
    position: absolute; top: 429px; width: 100%; text-align: center;
    font-size: 19px; color: var(--gold);
  }

  .contact {
    position: absolute; width: 100%; text-align: center;
    display: flex; flex-direction: column; align-items: center;
  }
  .contact-icon {
    width: 30px; height: 30px; border-radius: 50%;
    background: var(--gold); display: flex; align-items: center; justify-content: center;
  }
  .contact-text { margin-top: 7px; font-size: 16px; color: var(--gold-light); }
  .contact--phone { top: 493px; }
  .contact--mail  { top: 562px; }
  .contact--web   { top: 628px; }

  .back-lockup {
    position: absolute; left: 65px; top: 317px;
    display: flex; align-items: center; gap: 16px;
  }
  .back-disc { position: relative; width: 104px; height: 104px; flex: none; }
  .back-lockup .brand-name {
    font-family: "Montserrat", sans-serif; font-weight: 500;
    font-size: 34px; color: var(--gold); white-space: nowrap;
  }
  .back-url {
    position: absolute; top: 647px; width: 100%; text-align: center;
    font-size: 19px; color: var(--gold);
  }
</style>
</head>
<body>
  <section class="card card--front">
    <div class="brand-disc front-disc"><span class="brand-name">Nox Studio</span></div>

    <h1 class="holder-name">DANIEL REYES</h1>
    <p class="holder-role">Event Photographer and Videographer</p>

    <div class="contact contact--phone">
      <span class="contact-icon">
        <svg width="16" height="16" viewBox="0 0 24 24"><path fill="#0b0a08" d="M6.6 10.8a15.1 15.1 0 0 0 6.6 6.6l2.2-2.2c.3-.3.7-.4 1-.2 1.1.4 2.3.6 3.6.6.6 0 1 .4 1 1V20c0 .6-.4 1-1 1A17 17 0 0 1 3 4c0-.6.4-1 1-1h3.5c.6 0 1 .4 1 1 0 1.3.2 2.5.6 3.6.1.3 0 .7-.2 1z"/></svg>
      </span>
      <span class="contact-text">5550 1234 8890</span>
    </div>
    <div class="contact contact--mail">
      <span class="contact-icon">
        <svg width="16" height="16" viewBox="0 0 24 24"><rect x="3" y="6" width="18" height="12" fill="none" stroke="#0b0a08" stroke-width="2"/><path d="M3 6l9 7 9-7" fill="none" stroke="#0b0a08" stroke-width="2"/></svg>
      </span>
      <span class="contact-text">dreyes@noxstudio.com</span>
    </div>
    <div class="contact contact--web">
      <span class="contact-icon">
        <svg width="18" height="18" viewBox="0 0 24 24" fill="none" stroke="#0b0a08" stroke-width="1.6"><circle cx="12" cy="12" r="9"/><ellipse cx="12" cy="12" rx="4" ry="9"/><path d="M3 12h18M5 7h14M5 17h14"/></svg>
      </span>
      <span class="contact-text">www.noxstudio.com</span>
    </div>
  </section>

  <section class="card card--back">
    <div class="back-lockup">
      <span class="brand-disc back-disc"></span>
      <span class="brand-name">Nox Studio</span>
    </div>
    <p class="back-url">www.noxstudio.com</p>
  </section>
</body>
</html>
```